Create a bold and border around my logo to make it pop and sign graphic design

I would like someone to create a sign graphic design so I can use on the side of my trucks and put on yard signs. I would to remove a lot of the white and add more of the orange and blue to give it more pop when cars drive past. I would like the services to be removed and for you to leave space for a mobile number that i would add later. I don’t want my logo changed at all. I just want colour and design to be added to the background so i can use it in signage. Same colour as on the sign

```html
<!DOCTYPE html>
<html lang="en">
<head>
<meta charset="UTF-8">
<title>Branchworthy – Vehicle &amp; Yard Sign</title>
<link rel="stylesheet" href="https://fonts.googleapis.com/css2?family=Montserrat:wght@600&family=Roboto:wght@400&display=swap">
<style>
  :root {
    --backdrop: #dcdcdc;
    --brand-blue: #034ea2;
    --brand-blue-light: #1e7fe0;
    --brand-orange: #f37321;
    --brand-orange-light: #fbb27a;
    --wordmark-blue: #3f57a6;
    --white: #ffffff;
    --ink: #111111;
  }
  * { margin: 0; padding: 0; box-sizing: border-box; }
  html, body {
    width: 1200px;
    height: 1000px;
    overflow: hidden;
    background: var(--backdrop);
  }
  .sign {
    position: absolute;
    left: 158px;
    top: 280px;
    width: 885px;
    height: 440px;
    overflow: hidden;
  }
  .band { position: absolute; left: 0; width: 100%; }
  .band--blue { top: 0; height: 165px; background: var(--brand-blue); }
  .band--white { top: 165px; height: 170px; background: var(--white); }
  .band--orange { top: 335px; height: 105px; background: var(--brand-orange); }

  .texture { position: absolute; }
  .texture--blue-right {
    left: 590px; top: 0; width: 300px; height: 165px;
    background: radial-gradient(ellipse at 55% 60%, rgba(30,127,224,0.55), rgba(30,127,224,0) 70%);
  }
  .texture--blue-left {
    left: 40px; top: 90px; width: 240px; height: 75px;
    background: radial-gradient(ellipse at 50% 80%, rgba(30,127,224,0.35), rgba(30,127,224,0) 70%);
  }
  .texture--orange-left {
    left: 20px; top: 335px; width: 220px; height: 90px;
    background: radial-gradient(ellipse at 40% 30%, rgba(251,178,122,0.55), rgba(251,178,122,0) 70%);
  }

  .emblem-disc {
    position: absolute;
    left: 347px;
    top: 53px;
    width: 190px;
    height: 190px;
    border-radius: 50%;
    background: var(--white);
  }

  .brand-name {
    position: absolute;
    left: 0;
    top: 235px;
    width: 100%;
    text-align: center;
    font-family: "Montserrat", sans-serif;
    font-weight: 600;
    font-size: 76px;
    line-height: 90px;
    letter-spacing: 1px;
    color: var(--wordmark-blue);
  }

  .contact-pill {
    position: absolute;
    left: 247px;
    top: 332px;
    width: 390px;
    height: 53px;
    border-radius: 27px;
    background: var(--white);
    font-family: "Roboto", sans-serif;
    font-weight: 400;
    font-size: 26px;
    line-height: 53px;
    text-align: center;
    color: var(--ink);
  }
</style>
</head>
<body>
  <div class="sign">
    <div class="band band--blue"></div>
    <div class="band band--white"></div>
    <div class="band band--orange"></div>

    <div class="texture texture--blue-right" role="img" aria-label="Halftone dot texture in light blue"></div>
    <div class="texture texture--blue-left" role="img" aria-label="Halftone dot texture in light blue"></div>
    <div class="texture texture--orange-left" role="img" aria-label="Halftone dot texture in light orange"></div>

    <div class="emblem-disc"></div>
    <div class="brand-name">BRANCHWORTHY</div>
    <div class="contact-pill">You can contact us here</div>
  </div>
</body>
</html>
```